Calder Mindworks Psychology website transfer from WIX to Wordpress

I have a website currently coded in WIX and I want it (or something like it or better) designed to be coded on Wordpress instead. The website should have mobile optimization so that it can be viewed on mobile devices.

The current website is at: www.caldermindworks.example

I'm not looking for versions of the website that are very different to what I already have, unless they improve on it aesthetically. I'm mainly looking to have a Wordpress version of this website that I built, away from the WIX ecosystem.

Target Market(s)

Psychology services clients

Coding

Coded - Design and coding required

Number of Pages Required

5+ page

Font styles to use
Serif

Requirements
Must have
• The finished product shoud match my website exactly.
Nice to have
• I'm happy to see new ideas that improve on the current website.
Should not have
• It should not be a different version of my website.

```html
<!DOCTYPE html>
<html lang="en">
<head>
<meta charset="utf-8">
<title>Calder Mindworks Psychology – Website Screens</title>
<link href="https://fonts.googleapis.com/css2?family=Playfair+Display:wght@400;600;700&family=Source+Sans+3:wght@400;600;700&display=swap" rel="stylesheet">
<style>
  :root {
    --green: #2f5a50;
    --ink: #2b2b2b;
    --white: #ffffff;
    --page: #ffffff;
    --photo-a: #8a5a44;
    --photo-b: #c8653f;
    --photo-c: #d9d2cc;
    --shadow: 0 6px 24px rgba(0,0,0,0.12);
    --serif: "Playfair Display", Georgia, serif;
    --sans: "Source Sans 3", Arial, sans-serif;
  }
  * { box-sizing: border-box; margin: 0; padding: 0; }
  html, body { width: 1200px; height: 829px; overflow: hidden; background: var(--page); }
  .stage { position: relative; width: 1200px; height: 829px; overflow: hidden; }
  .screen { position: absolute; background: var(--white); box-shadow: var(--shadow); overflow: hidden; }

  .brand { font-family: var(--sans); font-weight: 400; color: var(--green); line-height: 1.05; }
  .ornament { display: block; background: linear-gradient(90deg, transparent, rgba(47,90,80,0.45), transparent); height: 3px; border-radius: 2px; }
  .btn { position: absolute; display: flex; align-items: center; justify-content: center; border-radius: 20px; font-family: var(--sans); font-weight: 600; letter-spacing: 0.12em; white-space: nowrap; }
  .btn-solid { background: var(--green); color: var(--white); box-shadow: 0 2px 4px rgba(0,0,0,0.2); }
  .btn-outline { border: 1px solid var(--green); color: var(--green); background: var(--white); box-shadow: 0 1px 3px rgba(0,0,0,0.15); }

  /* Left mobile screen */
  .mobile-services { left: 185px; top: 0; width: 218px; height: 757px; }
  .mobile-services .btn { left: 65px; width: 90px; height: 25px; font-size: 9px; }
  .service-title { position: absolute; left: 0; width: 218px; top: 88px; text-align: center; font-family: var(--serif); font-weight: 600; font-size: 15px; line-height: 19px; color: var(--green); }
  .service-text { position: absolute; left: 16px; width: 186px; top: 153px; text-align: center; font-family: var(--sans); font-size: 9px; line-height: 14px; color: var(--ink); }
  .footer { position: absolute; left: 0; top: 293px; width: 218px; height: 464px; background: var(--green); color: var(--white); font-family: var(--sans); }
  .footer .brand { position: absolute; left: 8px; top: 48px; width: 140px; color: var(--white); font-size: 12px; }
  .footer-hours { position: absolute; left: 9px; top: 108px; font-size: 8.3px; line-height: 14px; }
  .footer-hours strong { font-weight: 700; }
  .footer-help { position: absolute; left: 9px; top: 195px; font-size: 8.3px; line-height: 14px; font-weight: 700; }
  .hotlines { position: absolute; left: 9px; top: 250px; list-style: none; font-size: 8.3px; line-height: 14.1px; white-space: nowrap; }
  .hotlines span { text-decoration: underline; }
  .social { position: absolute; left: 10px; top: 396px; display: flex; gap: 8px; }
  .social i { display: block; width: 10px; height: 10px; border-radius: 50%; border: 1.4px solid var(--white); }
  .rights { position: absolute; left: 9px; top: 440px; font-size: 6.8px; }

  /* Desktop screen */
  .desktop { left: 314px; top: 66px; width: 570px; height: 763px; }
  .desktop-header { position: absolute; left: 0; top: 0; width: 570px; height: 43px; }
  .desktop-header .brand { position: absolute; left: 24px; top: 12px; font-size: 10px; width: 100px; }
  .nav { position: absolute; right: 25px; top: 17px; display: flex; gap: 12px; font-family: var(--serif); font-size: 7.3px; color: var(--ink); }
  .hero-photo { position: absolute; left: 242px; top: 43px; width: 328px; height: 363px; }
  .hero-copy { position: absolute; left: 40px; top: 121px; width: 205px; }
  .hero-copy h1 { font-family: var(--serif); font-weight: 700; font-size: 22.5px; color: var(--green); line-height: 1; white-space: nowrap; }
  .hero-copy .roles { margin-top: 8px; font-family: var(--sans); font-size: 6.8px; line-height: 10.8px; color: var(--ink); }
  .hero-copy .ornament { width: 50px; margin-top: 12px; }
  .hero-copy .intro { margin-top: 14px; font-family: var(--sans); font-size: 9.1px; line-height: 14.3px; color: var(--ink); }
  .desktop .btn { top: 286px; height: 20px; font-size: 7.3px; }
  .desktop .btn-solid { left: 40px; width: 115px; }
  .desktop .btn-outline { left: 168px; width: 53px; }
  .about { position: absolute; left: 0; top: 406px; width: 570px; height: 312px; background: var(--green); color: var(--white); }
  .about h2 { position: absolute; left: 0; width: 570px; top: 42px; text-align: center; font-family: var(--serif); font-weight: 400; font-size: 21px; }
  .about .ornament { position: absolute; left: 255px; top: 82px; width: 58px; background: linear-gradient(90deg, transparent, rgba(120,180,150,0.7), transparent); }
  .about-col { position: absolute; top: 111px; width: 242px; font-family: var(--sans); font-size: 6.6px; line-height: 10.7px; }
  .about-col p + p { margin-top: 10.7px; }
  .about-left { left: 25px; }
  .about-right { left: 305px; }
  .photo-strip { position: absolute; left: 0; top: 718px; width: 570px; height: 45px; background: linear-gradient(90deg, #9c8f82, #b8a797 40%, #c4ab98 70%, #cdbcae); opacity: 0.85; }

  /* Right mobile screen */
  .mobile-home { left: 797px; top: 220px; width: 219px; height: 609px; }
  .mobile-home .brand { position: absolute; left: 8px; top: 13px; font-size: 9.5px; width: 90px; }
  .menu-icon { position: absolute; left: 192px; top: 18px; width: 15px; }
  .menu-icon i { display: block; height: 1.2px; background: var(--green); margin-bottom: 4.5px; }
  .mobile-copy { position: absolute; left: 11px; top: 65px; width: 176px; }
  .mobile-copy h1 { font-family: var(--serif); font-weight: 700; font-size: 19.5px; color: var(--green); line-height: 1; white-space: nowrap; }
  .mobile-copy .roles { margin-top: 9px; font-family: var(--sans); font-size: 6.2px; line-height: 10.4px; color: var(--ink); }
  .mobile-copy .ornament { width: 65px; margin-top: 17px; }
  .mobile-copy .intro { margin-top: 20px; font-family: var(--sans); font-size: 7.9px; line-height: 12.5px; color: var(--ink); }
  .mobile-home .btn-solid { left: 11px; top: 228px; width: 151px; height: 26px; font-size: 9.6px; }
  .mobile-home .btn-outline { left: 11px; top: 271px; width: 70px; height: 25px; font-size: 9.6px; }
  .mobile-photo { position: absolute; left: 0; top: 326px; width: 219px; height: 259px; background: linear-gradient(150deg, var(--photo-c) 0%, #b49a88 30%, var(--photo-b) 55%, var(--photo-a) 80%, #6f6259 100%); }
  .mobile-band { position: absolute; left: 0; top: 585px; width: 219px; height: 24px; background: var(--green); }
</style>
</head>
<body>
<div class="stage">

  <section class="screen mobile-services">
    <a class="btn btn-outline" style="top:10px">Learn more</a>
    <h3 class="service-title">Training and<br>Consultation</h3>
    <span class="ornament" role="img" aria-label="Leafy vine ornament" style="position:absolute;left:84px;top:137px;width:50px"></span>
    <p class="service-text">Psychological assessment, counselling, and therapy using and evidence-based integrative interventions</p>
    <a class="btn btn-outline" style="top:225px">Learn more</a>

    <footer class="footer">
      <div class="brand">Calder Mindworks Psychology</div>
      <p class="footer-hours"><strong>Practice Hours<br>(by appointment only):</strong><br>Mondays 9:30am - 3:30pm<br>Thursdays: 8:30am - 2:30pm</p>
      <p class="footer-help">If you need support between<br>appointments or after hours,<br>&nbsp;please consider contacting:</p>
      <ul class="hotlines">
        <li><span>Careline</span> on 13 00 01</li>
        <li><span>Youth Talkline</span> on 1800 000 101</li>
        <li><span>Menstalk Support</span> on 1300 000 202</li>
        <li><span>Crisis Call Return</span> on 1300 000 303</li>
        <li><span>Blue Horizon</span> on 1300 00 04 04</li>
        <li><span>Clearmind Youth</span> on 1800 000 505</li>
        <li><span>PrideLine</span> on 1800 000 606</li>
        <li><span>Yarning Line</span> on 13 00 07</li>
      </ul>
      <div class="social" aria-label="Social links"><i></i><i></i><i></i></div>
      <p class="rights">All Right Reserved</p>
    </footer>
  </section>

  <section class="screen desktop">
    <header class="desktop-header">
      <div class="brand">Calder Mindworks Psychology</div>
      <nav class="nav"><span>Home</span><span>About</span><span>Services</span><span>FAQs</span><span>Fees &amp; Rebates</span><span>Contact</span></nav>
    </header>

    <svg class="hero-photo" viewBox="0 0 328 363" role="img" aria-label="Photo of the psychologist seated in an armchair writing on a clipboard">
      <defs>
        <linearGradient id="heroTone" x1="0" y1="0" x2="1" y2="1">
          <stop offset="0" stop-color="#d6cdc6"/>
          <stop offset="0.35" stop-color="#b39a89"/>
          <stop offset="0.55" stop-color="#c8653f"/>
          <stop offset="0.8" stop-color="#8a5a44"/>
          <stop offset="1" stop-color="#6e625a"/>
        </linearGradient>
      </defs>
      <path d="M18 0 C-10 40 -5 110 35 160 C70 205 50 280 40 363 L0 363 L0 0 Z" fill="#e9e9e9" opacity="0.7"/>
      <path d="M40 0 C10 45 15 115 50 160 C85 210 60 285 58 363 L328 363 L328 0 Z" fill="url(#heroTone)"/>
    </svg>

    <div class="hero-copy">
      <h1>Dr Elias Calder</h1>
      <p class="roles">Clinical and Counselling Psychologist,<br>Clinical Psychosexual Therapist</p>
      <span class="ornament" role="img" aria-label="Leafy vine ornament"></span>
      <p class="intro">I am a Clinical and Counselling Psychologist, and accredited Clinical Psychosexual Therapist, with over 15 years’ experience working with adults and young people of all abilities and identities</p>
    </div>
    <a class="btn btn-solid">Book an Appointment</a>
    <a class="btn btn-outline">Contact</a>

    <section class="about">
      <h2>About Me</h2>
      <span class="ornament" role="img" aria-label="Leafy vine ornament"></span>
      <div class="about-col about-left">
        <p>My name is Elias (he/they) and I am a Clinical and Counselling Psychologist, and accredited Clinical Psychosexual Therapist, with over 15 years’ experience working with adults and young people of all abilities and identities.</p>
        <p>My practice focuses on sex therapy and working with diversity, which regularly includes supporting members of LGBTQIA+, neurodivergent, and disabled communities. Because of this work, I am sex-positive and kink-, polyamory-, LGBTQIA+ and neurodiversity knowledgeable and affirming in my practice. I am also a member of many lived experience communities as part of my commitment to lifelong learning and honoring lived experience.</p>
        <p>I know that seeing a therapist can sometimes be anxiety-evoking, and as such, I always aim to curate a non-judgmental, collaborative, and intentional approach to working with people toward their personal goals and a life of value.</p>
      </div>
      <div class="about-col about-right">
        <p>In my work, I balance supportive counselling with evidence-based therapies such as: humanistic therapy, cognitive-behavioural therapy, acceptance and commitment therapy, compassion-focused therapy, and solution-focused counselling. My work is also underpinned by intersectional feminist and social justice frameworks. As part of ensuring that you are benefiting from our sessions, I will regularly check in to see if you’re finding your sessions useful, to ensure you feel understood, respected, and that your sessions are on track.</p>
        <p>In addition to my client work, I am also a board accredited Supervisor and enjoy supporting and supervising the practice of other clinicians, both new and experienced. And enjoy consultancy and training work with a range of organisations.</p>
      </div>
    </section>
    <div class="photo-strip" role="img" aria-label="Row of photos showing smiling people"></div>
  </section>

  <section class="screen mobile-home">
    <div class="brand">Calder Mindworks Psychology</div>
    <div class="menu-icon" aria-label="Menu"><i></i><i></i><i></i></div>
    <div class="mobile-copy">
      <h1>Dr Elias Calder</h1>
      <p class="roles">Clinical and Counselling Psychologist,<br>Clinical Psychosexual Therapist</p>
      <span class="ornament" role="img" aria-label="Leafy vine ornament"></span>
      <p class="intro">I am a Clinical and Counselling Psychologist, and accredited Clinical Psychosexual Therapist, with over 15 years’ experience working with adults and young people of all abilities and identities</p>
    </div>
    <a class="btn btn-solid">Book an Appointment</a>
    <a class="btn btn-outline">Contact</a>
    <div class="mobile-photo" role="img" aria-label="Photo of the psychologist seated in an armchair writing on a clipboard"></div>
    <div class="mobile-band"></div>
  </section>

</div>
</body>
</html>
```